Logo/Business Card design for a Chef using Tattoo Inspiration- Design must meet business card requirements on Pellu's website - link below

Business Card/Logo Design for my little brother- I would like to design and order my brother business cards for his business. He has a passion for cooking and was recently promoted to head chef. I have a picture of his tattoo that I would like re-imagined so it can be incorporate in the design of the business card or used to create a logo.
Must haves
1. Tattoo incorporated into the design
2. card Details below
must be able to use design to create the business card on Pellu.
Card details:
Business Name: Spoon And Ember
Name: Dennis Holloway
Title: Private Chef
Phone: 408-555-0172
Instragram: spoon_and_ember

optional use: via text or pictures incorporated in card design.
specialized in Korean, Italian, Peruvian, American, Chinese.
Private Chef
Dinner Parties
Special Occasions

type of card Square with round edges: the picture of his tattoo incorporated within the design.
Square Business Card templates to download https://help.pellu-example.com/hc/en-us/articles/500000001-Square-Business-Card-templates-to-download
Create business card here using their requirements.
https://www.pellu-example.com/us/design-templates/business-cards/?finishingOption=square_corners&laminate=mattelam&origPaperType=classic&paperType=classic&productType=businesscard_us
Card details

```html
<!DOCTYPE html>
<html lang="en">
<head>
<meta charset="utf-8">
<title>Spoon And Ember — Square Business Cards</title>
<link href="https://fonts.googleapis.com/css2?family=Oswald:wght@500;700&family=Montserrat:wght@600&display=swap" rel="stylesheet">
<style>
  :root {
    --backdrop: #dfe7e1;
    --card: #050505;
    --ink-light: #ffffff;
    --accent-red: #e3161f;
    --frame: #f2f2f2;
  }
  * { margin: 0; padding: 0; box-sizing: border-box; }
  html, body { width: 1200px; height: 900px; overflow: hidden; }
  body {
    background: var(--backdrop);
    position: relative;
    font-family: "Montserrat", sans-serif;
  }
  .card {
    position: absolute;
    width: 420px;
    height: 420px;
    background: var(--card);
    border-radius: 10px;
  }
  .card--front { left: 150px; top: 250px; }
  .card--back { left: 630px; top: 230px; }

  .card__frame {
    position: absolute;
    inset: 17px;
    border: 1.5px solid var(--frame);
  }

  .brand {
    display: flex;
    align-items: center;
    justify-content: center;
    gap: 12px;
  }
  .brand__dot {
    width: 16px; height: 16px;
    border-radius: 50%;
    background: var(--accent-red);
    flex: none;
  }
  .brand__name {
    font-family: "Oswald", sans-serif;
    font-weight: 700;
    font-size: 30px;
    letter-spacing: 1px;
    color: var(--ink-light);
    text-transform: uppercase;
  }
  .card--front .brand {
    position: absolute;
    left: 0; right: 0; top: 180px;
  }
  .card--back .brand {
    position: absolute;
    left: 0; right: 0; top: 50px;
  }

  .person {
    position: absolute;
    left: 0; right: 0; top: 148px;
    text-align: center;
  }
  .person__name {
    font-family: "Oswald", sans-serif;
    font-weight: 700;
    font-size: 30px;
    color: var(--accent-red);
    text-transform: uppercase;
    letter-spacing: 0.5px;
  }
  .person__title {
    display: inline-block;
    margin-top: 4px;
    padding: 0 18px 7px;
    font-size: 14px;
    font-weight: 600;
    color: var(--ink-light);
    text-transform: uppercase;
    border-bottom: 2px solid var(--accent-red);
    width: 178px;
  }

  .contacts {
    position: absolute;
    left: 0; right: 0; top: 317px;
    display: flex;
    justify-content: center;
    gap: 24px;
  }
  .contact {
    display: flex;
    align-items: center;
    gap: 9px;
    color: var(--ink-light);
    font-size: 15px;
    font-weight: 600;
  }
  .contact__icon { width: 24px; height: 24px; flex: none; }
</style>
</head>
<body>

  <section class="card card--front" aria-label="Card front">
    <div class="card__frame"></div>
    <div class="brand">
      <span class="brand__dot"></span>
      <span class="brand__name">Spoon And Ember</span>
    </div>
  </section>

  <section class="card card--back" aria-label="Card back">
    <div class="brand">
      <span class="brand__dot"></span>
      <span class="brand__name">Spoon And Ember</span>
    </div>

    <div class="person">
      <h1 class="person__name">Dennis Holloway</h1>
      <p class="person__title">Private Chef</p>
    </div>

    <div class="contacts">
      <div class="contact">
        <svg class="contact__icon" viewBox="0 0 24 24" aria-hidden="true">
          <circle cx="12" cy="12" r="10.5" fill="none" stroke="var(--accent-red)" stroke-width="2"/>
          <path d="M9 6.8 L10.6 9.6 L9.4 10.8 C10.1 12.4 11.6 13.9 13.2 14.6 L14.4 13.4 L17.2 15 L16.2 17 C12 17.3 6.7 12 7 7.8 Z" fill="var(--accent-red)"/>
        </svg>
        <span>408-555-0172</span>
      </div>
      <div class="contact">
        <svg class="contact__icon" viewBox="0 0 24 24" aria-hidden="true">
          <circle cx="12" cy="12" r="10.5" fill="none" stroke="var(--accent-red)" stroke-width="2"/>
        </svg>
        <span>spoon_and_ember</span>
      </div>
    </div>
  </section>

</body>
</html>
```